Business Card Design Project

We consult with hotels on setting rates and maximizing a revenue strategy

Industry/Entity Type

Business

Contact Information for Business Card

I am not sure what I want. Our company offers high level consulting to hotels around the country but we are also laid back. I would like something that is professional but also shows the laid back side

```html
<!DOCTYPE html>
<html lang="en">
<head>
<meta charset="utf-8">
<title>Harborline Business Card</title>
<link rel="stylesheet" href="https://fonts.googleapis.com/css2?family=Barlow:wght@400;500;700&display=swap">
<style>
  :root {
    --teal: #2f8a80;
    --teal-faint: #5ea9a0;
    --white: #ffffff;
    --ink: #3b2f2b;
    --text-dark: #2b2b2b;
    --backdrop: #e4e4e4;
  }
  * { box-sizing: border-box; margin: 0; padding: 0; }
  html, body { width: 1200px; height: 1026px; overflow: hidden; }
  body {
    background: var(--backdrop);
    font-family: "Barlow", Arial, sans-serif;
    position: relative;
  }
  .card {
    position: absolute;
    left: 250px;
    width: 700px;
    height: 400px;
    overflow: hidden;
    box-shadow: 0 4px 14px rgba(0,0,0,0.15);
  }
  /* Back side */
  .card-back {
    top: 90px;
    background: var(--teal);
    color: var(--white);
  }
  .card-back .brand {
    position: absolute;
    left: 190px;
    top: 118px;
  }
  .card-back .brand-name {
    font-weight: 700;
    font-size: 72px;
    letter-spacing: 1px;
    line-height: 1;
    white-space: nowrap;
  }
  .card-back .brand-tagline {
    font-weight: 500;
    font-size: 26px;
    margin-top: 6px;
    white-space: nowrap;
  }
  .card-back .web {
    position: absolute;
    left: 44px;
    bottom: 46px;
    font-size: 44px;
    color: var(--teal-faint);
    white-space: nowrap;
  }
  /* Front side */
  .card-front {
    top: 536px;
    display: flex;
    background: var(--white);
  }
  .front-left {
    width: 42%;
    flex: none;
    background: var(--white);
    display: flex;
    flex-direction: column;
    justify-content: center;
    padding: 0 22px 0 28px;
  }
  .logo-lockup { display: flex; align-items: center; gap: 10px; }
  .logo-mark { width: 28px; height: 28px; background: var(--teal); flex: none; }
  .logo-name {
    font-weight: 700;
    font-size: 30px;
    color: var(--ink);
    letter-spacing: 0.5px;
    line-height: 1;
    white-space: nowrap;
  }
  .logo-tagline {
    font-size: 12px;
    color: var(--ink);
    margin: 6px 0 0 38px;
    white-space: nowrap;
  }
  .front-left .web {
    margin-top: 24px;
    font-size: 19px;
    color: var(--text-dark);
    white-space: nowrap;
  }
  .front-right {
    flex: 1;
    background: var(--teal);
    color: var(--white);
    padding: 148px 0 0 28px;
    font-size: 20px;
    line-height: 1.3;
  }
  .person-name, .person-title { font-weight: 700; }
  .person-name { text-transform: uppercase; }
  .contact-list { margin-top: 22px; list-style: none; }
</style>
</head>
<body>
  <section class="card card-back" aria-label="Business card back">
    <div class="brand">
      <div class="brand-name">HARBORLINE</div>
      <div class="brand-tagline">Revenue Management Solutions</div>
    </div>
    <div class="web">www.HarborlineRMS.com</div>
  </section>

  <section class="card card-front" aria-label="Business card front">
    <div class="front-left">
      <div class="logo-lockup">
        <span class="logo-mark"></span>
        <span class="logo-name">HARBORLINE</span>
      </div>
      <div class="logo-tagline">Revenue Management Solutions</div>
      <div class="web">www.HarborlineRMS.com</div>
    </div>
    <div class="front-right">
      <div class="person-name">Dana Whitmore</div>
      <div class="person-title">Regional Revenue Manager</div>
      <ul class="contact-list">
        <li>Office 555-014-2287</li>
        <li>Fax 555-014-3390</li>
        <li>Dana@HarborlineRMS.com</li>
      </ul>
    </div>
  </section>
</body>
</html>
```